Brisk Venture - Logo & Business Card

I have briefly designed a logo for my small events business and need it fixed up. I would prefer it to be white on black background. I also need a PDF for business cards, I would like them to be black with the logo on one side and my details on the other side:

Brisk Venture
Corinna-May Feltwell
Founder / Director
0471 820 237
corinna@briskventure.com.au

```html
<!DOCTYPE html>
<html lang="en">
<head>
<meta charset="UTF-8">
<title>Brisk Venture – Business Card</title>
<link rel="stylesheet" href="https://fonts.googleapis.com/css2?family=Arimo:wght@400;700&display=swap">
<style>
  :root {
    --page: #ffffff;
    --card: #000000;
    --ink: #ffffff;
  }
  * { margin: 0; padding: 0; box-sizing: border-box; }
  html, body {
    width: 1056px;
    height: 1200px;
    overflow: hidden;
    background: var(--page);
    font-family: "Arimo", Arial, sans-serif;
    color: var(--ink);
  }
  .canvas {
    position: relative;
    width: 1056px;
    height: 1200px;
  }
  .card {
    position: absolute;
    left: 116px;
    width: 820px;
    height: 468px;
    background: var(--card);
    overflow: hidden;
  }
  .card--front { top: 100px; }
  .card--back { top: 628px; }

  .brand {
    position: absolute;
    display: flex;
    align-items: center;
    gap: 14px;
    font-weight: 700;
    color: var(--ink);
    white-space: nowrap;
  }
  .brand__dot {
    border-radius: 50%;
    background: var(--ink);
    flex: none;
  }
  .card--front .brand {
    left: 50%;
    top: 234px;
    transform: translate(-50%, -50%);
    font-size: 44px;
  }
  .card--front .brand__dot { width: 22px; height: 22px; }

  .card--back .brand {
    left: 66px;
    top: 142px;
    font-size: 26px;
    gap: 10px;
  }
  .card--back .brand__dot { width: 14px; height: 14px; }

  .identity {
    position: absolute;
    right: 66px;
    top: 62px;
    text-align: right;
  }
  .identity__name {
    font-size: 22px;
    font-weight: 700;
    line-height: 1.2;
  }
  .identity__role {
    font-size: 19.5px;
    font-weight: 400;
    line-height: 1.3;
  }

  .contact-band {
    position: absolute;
    left: 0;
    right: 0;
    top: 334px;
    height: 72px;
    border-top: 2px solid var(--ink);
    border-bottom: 2px solid var(--ink);
    display: flex;
    align-items: center;
    justify-content: center;
    gap: 26px;
  }
  .contact {
    display: flex;
    align-items: center;
    gap: 8px;
    font-size: 21px;
  }
  .contact__icon { width: 24px; height: 24px; flex: none; }
</style>
</head>
<body>
<main class="canvas">
  <section class="card card--front" aria-label="Card front">
    <div class="brand"><span class="brand__dot"></span>Brisk Venture</div>
  </section>

  <section class="card card--back" aria-label="Card back">
    <div class="brand"><span class="brand__dot"></span>Brisk Venture</div>

    <div class="identity">
      <p class="identity__name">Corinna-May Feltwell</p>
      <p class="identity__role">Founder / Director</p>
    </div>

    <div class="contact-band">
      <p class="contact">
        <svg class="contact__icon" viewBox="0 0 24 24" aria-hidden="true">
          <circle cx="12" cy="12" r="12" fill="#fff"/>
          <path d="M6 10.5c0-2 2.7-3.5 6-3.5s6 1.5 6 3.5v.8h-3v-1.6h-6v1.6H6z" fill="#000"/>
          <path d="M8.5 12.5h7l1.5 4.5H7z" fill="#000"/>
          <circle cx="12" cy="14.6" r="1.3" fill="#fff"/>
        </svg>
        0471 820 237
      </p>
      <p class="contact">
        <svg class="contact__icon" viewBox="0 0 24 24" aria-hidden="true">
          <circle cx="12" cy="12" r="12" fill="#fff"/>
          <rect x="6" y="8" width="12" height="8.5" fill="#000"/>
          <path d="M6.6 8.6 12 13l5.4-4.4" fill="none" stroke="#fff" stroke-width="1"/>
        </svg>
        corinna@briskventure.com.au
      </p>
    </div>
  </section>
</main>
</body>
</html>
```